THE AMBER HEARTH SESSIONS - CD COVER DESIGN

I am a professional female vocalist based in Devon, UK. I require a CD COVER for a CHRISTMAS album of mixed genre tracks - jazz/big-band/country/gospel/acoustic songs, all with a traditional 'Festive/Christmas' theme.

Cover to fit STANDARD CD JEWEL CASE comprising: FRONT COVER INLAY / INSIDE FRONT / REAR INLAY and SPINE. Plus CD FACE.

The design needs to incorporate the 2 publicity photographs attached. CD1 (wearing WHITE FUR JACKET) is the main picture and preferred choice for front cover pic. CD2 (wearing RED DRESS) can be used anywhere in the design.

CD WORDING: Please see attached info. The track listing is also provided on a separate sheet.
Updates

Sick

Target Market(s)

Festive music market!

Industry/Entity Type

It Professional

Font styles to use
Serif
Sans Serif
Decorative
Script

Colors
ec1f27

Requirements
Must have
• CHRISTMAS / FESTIVE THEME!
• Must incorporate the 2 publicity photographs attached.
• TRACK LISTING to feature on CD FACE and REAR INLAY.
• CD WORDING attached.
Should not have
• Not keen on 'cartoon type' images - prefer more traditional.

```html
<!DOCTYPE html>
<html lang="en">
<head>
<meta charset="utf-8">
<title>The Amber Hearth Sessions – CD Jewel Case Artwork</title>
<link rel="stylesheet" href="https://fonts.googleapis.com/css2?family=Cinzel:wght@500;700&family=Cormorant+Garamond:wght@400&family=Open+Sans:wght@400;700&family=Caveat+Brush&display=swap">
<style>
  :root{
    --red:#ec1f27;
    --red-deep:#b0101a;
    --red-dark:#7d0a12;
    --gold:#d9a94a;
    --cream:#f6e9dc;
    --ink:#ffffff;
    --page:#ffffff;
    --pine:#1f4a2a;
  }
  *{box-sizing:border-box;margin:0;padding:0}
  html,body{width:1200px;height:1200px;overflow:hidden;background:var(--page)}
  .sheet{position:absolute;left:40px;top:108px;width:1120px;height:984px}
  .panel{position:absolute;overflow:hidden}
  .disc-panel{left:0;top:0;width:570px;height:495px;background:radial-gradient(circle at 45% 45%,var(--red) 0%,var(--red-deep) 70%,var(--red-dark) 100%)}
  .inside-panel{left:570px;top:0;width:550px;height:495px;background:radial-gradient(circle at 50% 50%,var(--red) 0%,var(--red-deep) 75%)}
  .rear-panel{left:0;top:495px;width:550px;height:489px;background:radial-gradient(circle at 45% 40%,var(--red) 0%,var(--red-deep) 70%,var(--red-dark) 100%)}
  .spine{left:550px;top:495px;width:24px;height:489px;background:var(--red)}
  .front-panel{left:574px;top:495px;width:546px;height:489px}

  /* CD face */
  .case-tab{position:absolute;width:90px;height:90px;border-radius:50%;background:rgba(246,220,210,.55)}
  .disc{position:absolute;left:60px;top:30px;width:440px;height:440px;border-radius:50%;overflow:hidden;background:var(--cream);box-shadow:0 0 0 2px rgba(255,255,255,.4)}
  .disc-photo{position:absolute;left:0;top:0;width:440px;height:440px;
    clip-path:polygon(0 0,262px 0,262px 292px,100% 292px,100% 100%,0 100%);
    background:radial-gradient(circle at 35% 28%,#f3dcc6 0%,#d9b59a 28%,#c8283a 58%,#a5101c 100%)}
  .disc-hole{position:absolute;left:176px;top:176px;width:88px;height:88px;border-radius:50%;background:rgba(255,255,255,.35);border:1px solid rgba(255,255,255,.7)}
  .disc-hole::after{content:"";position:absolute;left:26px;top:26px;width:34px;height:34px;border-radius:50%;background:var(--red);border:2px solid #fff}
  .disc-tracks-head{position:absolute;left:270px;top:80px;width:116px;text-align:center;font:400 9px "Cormorant Garamond",serif;color:var(--red-deep);letter-spacing:.5px}
  .disc-tracks{position:absolute;left:270px;top:94px;width:116px;text-align:center;font:400 5.2px/7.8px "Open Sans",sans-serif;color:var(--red-deep);list-style:none}
  .disc-theme{position:absolute;left:40px;top:330px;transform:rotate(-90deg);transform-origin:left top;font:400 20px "Cormorant Garamond",serif;color:rgba(255,255,255,.85);letter-spacing:2px;white-space:nowrap}
  .disc-title{position:absolute;left:85px;top:300px;width:270px;text-align:center;font:700 24px/34px "Cinzel",serif;color:var(--gold);text-shadow:0 1px 2px rgba(90,0,0,.6)}
  .disc-artist{position:absolute;left:85px;top:374px;width:270px;text-align:center;font:400 10px "Open Sans",sans-serif;color:#fff;letter-spacing:.5px}

  /* Inside front */
  .garland{position:absolute}
  .garland-top{left:0;top:0;width:250px;height:150px;border-radius:0 0 100% 0;background:radial-gradient(ellipse at 0 0,#2d5a33 0%,var(--pine) 50%,rgba(31,74,42,0) 75%)}
  .garland-bottom{right:0;bottom:0;width:300px;height:260px;border-radius:100% 0 0 0;background:radial-gradient(ellipse at 100% 100%,#2d5a33 0%,var(--pine) 45%,rgba(31,74,42,0) 72%)}
  .inside-copy{position:absolute;left:60px;top:110px;width:400px;transform:rotate(180deg);color:var(--ink);font:400 10px/14px "Open Sans",sans-serif;text-align:left}
  .inside-copy strong{font-weight:700}
  .inside-copy .guild{margin-top:12px;font-weight:700}
  .guild-mark{display:flex;align-items:center;gap:6px;margin:8px 0 14px;font:700 16px "Open Sans",sans-serif}
  .guild-mark span.sq{width:12px;height:12px;background:#fff}
  .booking{font-weight:700}
  .social-row{display:flex;gap:6px;margin-top:10px}
  .social-row span{width:15px;height:15px;border-radius:50%;background:#fff}

  /* Rear inlay */
  .ornament{position:absolute;width:130px;height:110px;background:radial-gradient(ellipse at center,rgba(255,214,200,.28) 0%,rgba(255,214,200,0) 70%)}
  .track-list{position:absolute;left:0;top:52px;width:550px;list-style:none;text-align:center;font:700 9.6px/17.4px "Open Sans",sans-serif;color:#fff;padding-left:40px;padding-right:80px}
  .track-list li.gap{margin-top:6px}

  /* Spine */
  .spine-title{position:absolute;left:5px;top:20px;writing-mode:vertical-rl;font:400 17px "Caveat Brush",cursive;color:#fff;white-space:nowrap}
  .spine-artist{position:absolute;left:6px;top:330px;writing-mode:vertical-rl;font:400 8.5px "Open Sans",sans-serif;color:#fff;letter-spacing:.5px}

  /* Front cover */
  .cover-photo{position:absolute;inset:0;background:radial-gradient(circle at 55% 40%,#f2dcc8 0%,#e9d6bd 25%,#d8c5ad 45%,#6a2a1e 75%,#3b1e14 100%)}
  .cover-theme{position:absolute;right:10px;top:8px;writing-mode:vertical-rl;font:400 44px "Cormorant Garamond",serif;color:rgba(255,255,255,.85);letter-spacing:1px;white-space:nowrap}
  .cover-title{position:absolute;left:40px;top:330px;width:420px;font:400 30px/1 "Caveat Brush",cursive;color:var(--red-deep);transform:rotate(-4deg)}
  .cover-title .big{display:block;font-size:64px;margin-top:4px;margin-left:-8px}
  .cover-artist{position:absolute;left:300px;top:445px;font:400 17px "Open Sans",sans-serif;color:var(--red)}
</style>
</head>
<body>
<main class="sheet">

  <section class="panel disc-panel" aria-label="CD face">
    <span class="case-tab" style="left:40px;top:30px"></span>
    <span class="case-tab" style="left:430px;top:30px"></span>
    <span class="case-tab" style="left:40px;top:380px"></span>
    <span class="case-tab" style="left:430px;top:380px"></span>
    <div class="disc">
      <div class="disc-photo" role="img" aria-label="Publicity photograph of the singer in a red dress"></div>
      <p class="disc-tracks-head">SONGS TRACK</p>
      <ol class="disc-tracks">
        <li>01. JINGLE BELLS</li><li>02. HARK THE HERALD ANGELS SING</li><li>03. DO YOU HEAR WHAT I HEAR</li><li>04. WINTER WONDERLAND</li><li>05. I'VE GOT MY LOVE TO KEEP ME WARM</li><li>06. THE FIRST NOEL</li><li>07. LITTLE DRUMMER BOY</li><li>08. BABY ITS COLD OUTSIDE</li><li>09. TENNESSEE CHRISTMAS</li><li>10. HAVE A HOLLY JOLLY CHRISTMAS</li><li>11. SANTA BABY</li><li>12. BLUE CHRISTMAS</li><li>13. THE CHRISTMAS SONG</li><li>14. O COME ALL YE FAITHFUL</li><li>15. HAVE YOURSELF A MERRY LITTLE CHRISTMAS</li><li>16. LET IT SNOW</li><li>17. IN THE BLEAK MIDWINTER</li><li>18. MARY'S BOY CHILD</li><li>19. WHITE CHRISTMAS</li><li>20. SANTA CLAUS IS COMIN' IN A BOOGIE WOOGIE CHOO-CHOO TRAIN</li>
      </ol>
      <div class="disc-hole"></div>
      <p class="disc-theme">FESTIVE THEME!</p>
      <h2 class="disc-title">THE AMBER HEARTH SESSIONS</h2>
      <p class="disc-artist">MARIBEL FROST</p>
    </div>
  </section>

  <section class="panel inside-panel" aria-label="Inside front inlay">
    <div class="garland garland-top" role="img" aria-label="Pine garland with gold snowflakes and baubles"></div>
    <div class="garland garland-bottom" role="img" aria-label="Pine garland with gold snowflakes and baubles"></div>
    <div class="inside-copy">
      <p><strong>MARIBEL FROST</strong> is a British PROFESSIONAL SINGER and award winning International MULTI-TRIBUTE ARTISTE.<br>Available for bookings in the UK &amp; WORLDWIDE.</p>
      <p class="guild">Member of PERFORMERS GUILD.</p>
      <div class="guild-mark"><span class="sq"></span>Performers Guild</div>
      <p class="booking">BOOKING ENQUIRIES:</p>
      <p><strong>Telephone:</strong> 07700 900 412</p>
      <p><strong>Email:</strong> bookings@maribelfrost.example</p>
      <div class="social-row"><span></span><span></span><span></span><span></span><span></span><span></span><span></span></div>
    </div>
  </section>

  <section class="panel rear-panel" aria-label="Rear inlay">
    <div class="ornament" role="img" aria-label="Cream flourish ornament" style="left:70px;top:20px"></div>
    <div class="ornament" role="img" aria-label="Cream flourish ornament" style="left:330px;top:20px"></div>
    <div class="ornament" role="img" aria-label="Cream flourish ornament" style="left:70px;top:360px"></div>
    <div class="ornament" role="img" aria-label="Cream flourish ornament" style="left:330px;top:360px"></div>
    <ol class="track-list">
      <li>01. JINGLE BELLS</li><li>02. HARK THE HERALD ANGELS SING</li><li>03. DO YOU HEAR WHAT I HEAR</li><li>04. WINTER WONDERLAND</li><li>05. I'VE GOT MY LOVE TO KEEP ME WARM</li><li>06. THE FIRST NOEL</li><li>07. LITTLE DRUMMER BOY</li><li>08. BABY ITS COLD OUTSIDE</li><li>09. TENNESSEE CHRISTMAS</li><li>10. HAVE A HOLLY JOLLY CHRISTMAS</li>
      <li class="gap">11. SANTA BABY</li><li>12. BLUE CHRISTMAS</li><li>13. THE CHRISTMAS SONG</li><li>14. O COME ALL YE FAITHFUL</li><li>15. HAVE YOURSELF A MERRY LITTLE CHRISTMAS</li><li>16. LET IT SNOW</li><li>17. IN THE BLEAK MIDWINTER</li><li>18. MARY'S BOY CHILD</li><li>19. WHITE CHRISTMAS</li><li>20. SANTA CLAUS IS COMIN' IN A BOOGIE<br>WOOGIE CHOO-CHOO TRAIN</li>
    </ol>
  </section>

  <section class="panel spine" aria-label="Spine">
    <p class="spine-title">THE AMBER HEARTH SESSIONS</p>
    <p class="spine-artist">MARIBEL FROST</p>
  </section>

  <section class="panel front-panel" aria-label="Front cover">
    <div class="cover-photo" role="img" aria-label="Publicity photograph of the singer in a white fur jacket before a decorated Christmas tree"></div>
    <p class="cover-theme">FESTIVE THEME!</p>
    <h1 class="cover-title">THE AMBER HEARTH<span class="big">SESSIONS</span></h1>
    <p class="cover-artist">MARIBEL FROST</p>
  </section>

</main>
</body>
</html>
```